VORN - Business cards

Business card to be created for Commercial sales staff

Target Market(s)

Commercial businesses

Industry/Entity Type

Commercial

Contact Information for Business Card

Look professional. For commercial clients

Colors
ffffff

Requirements
Must have
• - Vorn Logo
• - Commercial sales staff as postion
• - room for commerical sales manager role
• - person name and their mobile number
• - Website : vornelectrical.com.au
Nice to have
• White background.
• On back of business card just have the logo no other information
Should not have
• Should only have white background on front of card.

```html
<!DOCTYPE html>
<html lang="en">
<head>
<meta charset="utf-8">
<title>VORN Business Cards</title>
<link rel="stylesheet" href="https://fonts.googleapis.com/css2?family=Montserrat:wght@400;500;800&display=swap">
<style>
:root{
  --charcoal:#33363d;
  --white:#ffffff;
  --red:#c8202b;
  --ink:#2b2d33;
  --ground:#e9e9eb;
}
*{margin:0;padding:0;box-sizing:border-box}
html,body{width:1200px;height:900px;overflow:hidden}
body{background:var(--ground);font-family:"Montserrat",sans-serif;position:relative}
.card{position:absolute;left:250px;width:700px;height:400px;border-radius:22px;overflow:hidden;box-shadow:0 8px 24px rgba(0,0,0,.18)}
.card-back{top:40px;background:var(--charcoal)}
.card-front{top:460px;background:var(--charcoal)}
.card-shape{position:absolute;inset:0}
.wordmark{display:flex;align-items:center;gap:14px;font-weight:800;letter-spacing:1px}
.wordmark-dot{border-radius:50%;background:var(--red)}
.card-back .wordmark{position:absolute;left:50%;top:48%;transform:translate(-50%,-50%);color:var(--white);font-size:92px}
.card-back .wordmark-dot{width:58px;height:58px}
.back-site{position:absolute;right:150px;bottom:52px;color:var(--white);font-size:17px}
.back-site b{font-weight:800}
.card-front .wordmark{position:absolute;right:40px;top:34px;color:var(--ink);font-size:74px}
.card-front .wordmark-dot{width:46px;height:46px}
.contact{position:absolute;right:40px;top:150px;text-align:right;color:var(--ink)}
.contact-name{color:var(--red);font-weight:500;font-size:26px;letter-spacing:1px;margin-bottom:6px}
.contact-role{font-size:15px;line-height:1.35}
.contact-list{list-style:none;margin-top:8px;font-size:15px;line-height:1.55}
.contact-list li{display:flex;justify-content:flex-end;align-items:center;gap:8px}
.contact-list svg{width:12px;height:12px;fill:var(--red)}
.contact-list .site-name{color:var(--red);font-weight:800}
</style>
</head>
<body>

<section class="card card-back">
  <div class="wordmark"><span class="wordmark-dot"></span>VORN</div>
  <p class="back-site">www.<b>vornelectrical</b>.com.au</p>
</section>

<section class="card card-front">
  <svg class="card-shape" viewBox="0 0 700 400" aria-hidden="true">
    <path fill="#c8202b" d="M238 0 C120 80 130 310 250 362 C340 398 500 382 585 372 C450 382 320 370 262 340 C170 290 170 90 262 0 Z"/>
    <path fill="#ffffff" d="M700 0 L700 350 C600 372 380 380 272 340 C180 300 175 80 270 0 Z"/>
  </svg>

  <div class="wordmark"><span class="wordmark-dot"></span>VORN</div>

  <div class="contact">
    <h1 class="contact-name">MAREK ELLISON</h1>
    <p class="contact-role">Commercial sales staff</p>
    <p class="contact-role">commerical sales manager</p>
    <ul class="contact-list">
      <li>+330 2815-4409
        <svg viewBox="0 0 24 24"><path d="M6.6 10.8a15 15 0 0 0 6.6 6.6l2.2-2.2c.3-.3.7-.4 1-.2 1.1.4 2.3.6 3.6.6.6 0 1 .4 1 1V20c0 .6-.4 1-1 1A17 17 0 0 1 3 4c0-.6.4-1 1-1h3.5c.6 0 1 .4 1 1 0 1.3.2 2.5.6 3.6.1.3 0 .7-.2 1z"/></svg>
      </li>
      <li>info@vornelectrical.com.au
        <svg viewBox="0 0 24 24"><path d="M2 5h20v14H2z M4 7v.5l8 5 8-5V7l-8 5z"/></svg>
      </li>
      <li><span>www.<span class="site-name">vornelectrical</span>.com.au</span>
        <svg viewBox="0 0 24 24"><circle cx="12" cy="12" r="10"/></svg>
      </li>
    </ul>
  </div>
</section>

</body>
</html>
```